https://dorvakel.com

We need a cool technology design for our Managed IT Services company. We are located in Coral Springs Florida. We provide all IT services and support for small to medium sized businesses. We would like to see designs that use our blue and white colors from our website.

```html
<!DOCTYPE html>
<html lang="en">
<head>
<meta charset="utf-8">
<title>Dorvakel Business Card</title>
<link href="https://fonts.googleapis.com/css2?family=Lato:wght@300;400;700;900&display=swap" rel="stylesheet">
<style>
  :root {
    --navy: #142f55;
    --blue: #0d5fb3;
    --white: #ffffff;
    --stage: #e0e0e0;
    --rule: #c9ccd2;
    --mint: #d8ecdf;
  }
  * { margin: 0; padding: 0; box-sizing: border-box; }
  html, body { width: 1200px; height: 1200px; overflow: hidden; }
  body { background: var(--stage); font-family: "Lato", sans-serif; position: relative; }

  .card { position: absolute; left: 210px; width: 779px; height: 419px; background: var(--white); overflow: hidden; }
  .card-front { top: 111px; }
  .card-back { top: 623px; }

  .side-tab { position: absolute; left: 0; top: 75px; width: 16px; height: 270px; background: var(--navy); border-radius: 0 12px 12px 0; }

  .wordmark { position: absolute; display: flex; align-items: center; gap: 14px; color: var(--navy); font-weight: 900; letter-spacing: -1px; line-height: 1; }
  .wordmark .mark-dot { border-radius: 50%; background: var(--navy); flex: none; }
  .card-front .wordmark { left: 40px; top: 188px; font-size: 58px; }
  .card-front .mark-dot { width: 18px; height: 18px; }
  .card-back .wordmark { left: 50%; top: 140px; transform: translateX(-50%); font-size: 92px; }
  .card-back .mark-dot { width: 26px; height: 26px; }

  .info-panel { position: absolute; left: 384px; top: 0; width: 395px; height: 419px; background: var(--navy); color: var(--white); }
  .company-title { position: absolute; left: 49px; top: 38px; font-size: 33px; font-weight: 900; letter-spacing: 0.2px; }
  .tagline { position: absolute; left: 49px; top: 97px; font-size: 27px; font-weight: 300; letter-spacing: 0.4px; }
  .title-rule { position: absolute; left: 50px; top: 148px; width: 78px; height: 4px; background: var(--rule); }

  .contact { position: absolute; left: 48px; display: flex; align-items: center; gap: 21px; font-size: 17px; }
  .contact .icon { width: 42px; height: 42px; border-radius: 50%; background: var(--blue); display: flex; align-items: center; justify-content: center; flex: none; }
  .contact-phone { top: 186px; }
  .contact-web { top: 249px; }
  .contact-address { top: 314px; align-items: flex-start; }
  .contact-address .icon { margin-top: 4px; }
  .contact-address p { line-height: 26.5px; margin-top: -7px; }

  .service-band { position: absolute; left: 0; bottom: 0; width: 779px; height: 96px; background: var(--navy); border-top: 4px solid #d5d8dd; }
  .service-item { position: absolute; display: flex; align-items: center; gap: 10px; color: var(--white); font-size: 13.5px; font-weight: 700; white-space: nowrap; }
  .service-item svg { flex: none; }
</style>
</head>
<body>

<section class="card card-front">
  <div class="side-tab"></div>
  <div class="wordmark"><span class="mark-dot"></span>DORVAKEL</div>

  <div class="info-panel">
    <h1 class="company-title">DORVAKEL FLORIDA</h1>
    <p class="tagline">IT SUPPOR EXPERTS</p>
    <div class="title-rule"></div>

    <div class="contact contact-phone">
      <span class="icon">
        <svg width="22" height="22" viewBox="0 0 24 24"><path fill="#fff" d="M3 9c0-3 4-5 9-5s9 2 9 5v2h-5V9c-1-.6-2.4-.9-4-.9S9 8.4 8 9v2H3z"/><path fill="#fff" d="M7 12h10l2 8H5z"/><g fill="#0d5fb3"><rect x="9" y="14" width="2" height="1.5"/><rect x="13" y="14" width="2" height="1.5"/><rect x="9" y="17" width="2" height="1.5"/><rect x="13" y="17" width="2" height="1.5"/></g></svg>
      </span>
      <span>(954) 555-0142</span>
    </div>

    <div class="contact contact-web">
      <span class="icon">
        <svg width="24" height="24" viewBox="0 0 24 24" fill="none" stroke="#fff" stroke-width="1.6"><circle cx="12" cy="12" r="8.5"/><path d="M4 9c4 1 8 5 9 11M7 5c3 3 4 7 3 11M18 5c-3 2-6 6-11 8"/><path d="M15 15l5 2-2 1-1 2z" fill="#fff"/></svg>
      </span>
      <span>https://dorvakel.com</span>
    </div>

    <div class="contact contact-address">
      <span class="icon">
        <svg width="20" height="24" viewBox="0 0 20 24"><path fill="#fff" d="M10 1a8 8 0 0 0-8 8c0 6 8 14 8 14s8-8 8-14a8 8 0 0 0-8-8z"/><circle cx="10" cy="9" r="3" fill="#0d5fb3"/></svg>
      </span>
      <p>Dorvakel<br>2718 N Harbor Ridge Dr #140<br>Coral Springs, Florida 33067</p>
    </div>
  </div>
</section>

<section class="card card-back">
  <div class="wordmark"><span class="mark-dot"></span>DORVAKEL</div>

  <div class="service-band">
    <div class="service-item" style="left:28px;top:16px"><svg width="16" height="14" viewBox="0 0 16 14"><polygon fill="#d8ecdf" points="4,0 12,0 16,7 12,14 4,14 0,7"/></svg>MANAGED IT SERVICES</div>
    <div class="service-item" style="left:28px;top:53px"><svg width="16" height="14" viewBox="0 0 16 14"><polygon fill="#d8ecdf" points="4,0 12,0 16,7 12,14 4,14 0,7"/></svg>IT SECURITY SERVICES</div>
    <div class="service-item" style="left:242px;top:16px"><svg width="16" height="14" viewBox="0 0 16 14"><polygon fill="#d8ecdf" points="4,0 12,0 16,7 12,14 4,14 0,7"/></svg>CLOUD COMPUTING SERVICES</div>
    <div class="service-item" style="left:242px;top:53px"><svg width="16" height="14" viewBox="0 0 16 14"><polygon fill="#d8ecdf" points="4,0 12,0 16,7 12,14 4,14 0,7"/></svg>INDUSTRY SPECIFIC &amp; DATA SERVICES</div>
    <div class="service-item" style="left:552px;top:16px"><svg width="16" height="14" viewBox="0 0 16 14"><polygon fill="#d8ecdf" points="4,0 12,0 16,7 12,14 4,14 0,7"/></svg>HARDWARE &amp; HARDWARE</div>
    <div class="service-item" style="left:552px;top:53px"><svg width="16" height="14" viewBox="0 0 16 14"><polygon fill="#d8ecdf" points="4,0 12,0 16,7 12,14 4,14 0,7"/></svg>BUSINESS COMMUNICATION</div>
  </div>
</section>

</body>
</html>
```